2013 Golf Outing Flyer

Our charitable organization was created in honor of my daughter who died at age 16. Our annual fundraiser is a golf tournament. I am not a creative person so I'd like someone to design a printable flyer that grabs people's attention but is not too busy while incorportating our organization's logo with the basic information.

Event details:
3rd Annual Marissa Joan Caldwell Memorial Golf Tournament
4 person scramble

Saturday October 5th, 2013
Larkspur Golf Club, Auburn, IL
9:30 Registration
Shotgun start at noon
To Register go online to www.marissajcaldwellgolf.teesignups.example or email
marissacaldwellfund@mailbox.example

Scholarships to Cedar Rapids Hollow High School seniors are made possible by our orgnization through this fundraiser.
Updates

Target Market(s)

golfers and businesses willing to sponsor event

Industry/Entity Type

School

Requirements
Must have
• single page-easy to print
includes non profit organization logo which I attached (think I did)
Specific information about the tournament- date and location and registration info
Nice to have
• company logo and the golf outing logo but if both are too much, then just the golf logo and the organization name can be at the bottom

```html
<!DOCTYPE html>
<html lang="en">
<head>
<meta charset="utf-8">
<title>3rd Annual Marissa Joan Caldwell Memorial Golf Tournament</title>
<link rel="stylesheet" href="https://fonts.googleapis.com/css2?family=Cormorant+Garamond:ital,wght@0,600;0,700;1,600;1,700&family=Libre+Baskerville:wght@700&display=swap">
<style>
  :root {
    --white: #ffffff;
    --lime: #c5d82a;
    --sky-top: #1f5fae;
    --sky-mid: #4f93d6;
    --grass: #5d9a2c;
    --green-dark: #1f5a25;
    --green-mid: #3f8a2e;
    --brown: #6b4a22;
    --ink: #333333;
  }
  * { margin: 0; padding: 0; box-sizing: border-box; }
  html, body { width: 927px; height: 1200px; overflow: hidden; background: var(--white); }
  .flyer { position: relative; width: 927px; height: 1200px; overflow: hidden; background: var(--white); }
  .backdrop { position: absolute; inset: 0; }

  .brand { position: absolute; left: 28px; top: 50px; display: flex; align-items: center; gap: 12px; }
  .brand-mark { width: 40px; height: 40px; border-radius: 50%; background: var(--lime); flex: none; }
  .brand-name { font-family: "Cormorant Garamond", serif; font-weight: 700; font-size: 26px; line-height: 1; color: var(--brown); }

  .headline { position: absolute; right: 20px; top: 425px; width: 720px; text-align: right; color: var(--white); font-family: "Cormorant Garamond", serif; font-style: italic; font-weight: 700; font-size: 41px; line-height: 1.2; text-shadow: 0 1px 3px rgba(0,0,0,.25); }
  .format { position: absolute; right: 26px; top: 540px; color: var(--white); font-family: "Libre Baskerville", serif; font-weight: 700; font-size: 24px; line-height: 1.2; letter-spacing: .5px; }

  .register { position: absolute; left: 27px; top: 982px; color: var(--white); }
  .register-title { font-family: "Cormorant Garamond", serif; font-style: italic; font-weight: 700; font-size: 50px; line-height: 1; margin-bottom: 14px; }
  .register-line { font-family: "Cormorant Garamond", serif; font-style: italic; font-weight: 600; font-size: 19px; line-height: 27px; }

  .details { position: absolute; right: 22px; top: 928px; text-align: right; color: var(--white); font-family: "Cormorant Garamond", serif; font-style: italic; font-weight: 700; }
  .details-date { font-size: 42px; line-height: 50px; }
  .details-line { font-size: 32px; line-height: 41px; }

  .footnote { position: absolute; left: 24px; top: 1138px; width: 400px; font-family: "Cormorant Garamond", serif; font-weight: 600; font-size: 15px; line-height: 1.25; color: var(--ink); }
</style>
</head>
<body>
<main class="flyer">
  <svg class="backdrop" width="927" height="1200" viewBox="0 0 927 1200">
    <defs>
      <linearGradient id="photoTone" x1="0" y1="0" x2="0" y2="1">
        <stop offset="0" stop-color="#1f5fae"/>
        <stop offset="0.45" stop-color="#4f93d6"/>
        <stop offset="0.6" stop-color="#8fbf4a"/>
        <stop offset="1" stop-color="#5d9a2c"/>
      </linearGradient>
      <linearGradient id="fieldGreen" x1="0" y1="0" x2="0" y2="1">
        <stop offset="0" stop-color="#3f8a2e"/>
        <stop offset="1" stop-color="#1f5a25"/>
      </linearGradient>
    </defs>
    <rect x="0" y="0" width="927" height="1136" fill="url(#photoTone)" role="img" aria-label="Photo of a woman golfer in a white cap and lime skirt driving from a fairway under a blue sky with clouds"/>
    <path class="swoosh-top" d="M0,282 C260,212 600,105 927,0 V38 C610,160 280,262 0,318 Z" fill="#c5d82a"/>
    <path class="header-field" d="M0,0 H858 C620,110 300,230 0,296 Z" fill="#ffffff"/>
    <path class="swoosh-bottom" d="M0,955 C320,900 690,790 927,650 V705 C700,835 310,940 0,982 Z" fill="#c5d82a"/>
    <path class="info-field" d="M0,975 C310,935 700,832 927,700 V1136 H0 Z" fill="url(#fieldGreen)"/>
  </svg>

  <div class="brand">
    <span class="brand-mark"></span>
    <span class="brand-name">MJC Memorial Golf Outing</span>
  </div>

  <h1 class="headline">3rd Annual Marissa Joan Caldwell<br>Memorial Golf Tournament</h1>
  <p class="format">4 person scramble</p>

  <section class="details">
    <p class="details-date">Saturday October 5th, 2013</p>
    <p class="details-line">Larkspur Golf Club, Auburn, IL</p>
    <p class="details-line">9:30 Registration</p>
    <p class="details-line">Shotgun start at noon</p>
  </section>

  <section class="register">
    <h2 class="register-title">To Register</h2>
    <p class="register-line">marissacaldwellfund@mailbox.example</p>
    <p class="register-line">www.marissajcaldwellgolf.teesignups.example</p>
  </section>

  <p class="footnote">Scholarships to Cedar Rapids Hollow High School seniors are made possible by our orgnization through this fundraiser.</p>
</main>
</body>
</html>
```